Torvane PT Business Card

I need the card to be bright/bold colours to stand out amongst others.
It needs to have my company logo.
I was not interested in pictures etc just a layout that attracts attention.

I have attached my old design which is very plain. I also needed change the contact details. And my description changed to Personal Trainer
Phone 0427309581
Facebook Torvane PT
No email address please, no street address.
And only Torvane PT (Please remove anything to do with Torvane Supplements)

```html
<!DOCTYPE html>
<html lang="en">
<head>
<meta charset="utf-8">
<title>Torvane PT Business Card</title>
<link rel="stylesheet" href="https://fonts.googleapis.com/css2?family=Open+Sans:wght@400;600;800&display=swap">
<style>
  :root {
    --brand-blue: #0d84c9;
    --brand-yellow: #f5d616;
    --ink: #444444;
    --card-white: #ffffff;
    --backdrop: #e9e9e9;
  }
  * { margin: 0; padding: 0; box-sizing: border-box; }
  html, body {
    width: 1200px;
    height: 987px;
    overflow: hidden;
    background: var(--backdrop);
    font-family: "Open Sans", sans-serif;
  }
  .card {
    position: absolute;
    left: 293px;
    width: 615px;
    height: 351px;
  }
  .card--front { top: 130px; background: var(--card-white); }
  .card--back { top: 506px; background: var(--brand-blue); }

  .wordmark {
    position: absolute;
    font-family: "Open Sans", sans-serif;
    font-weight: 800;
    font-size: 46px;
    line-height: 1;
    letter-spacing: 1px;
    text-transform: uppercase;
    white-space: nowrap;
  }
  .card--front .wordmark { left: 37px; top: 76px; color: var(--brand-blue); }
  .card--back .wordmark {
    left: 0; right: 0; top: 150px;
    text-align: center;
    color: var(--card-white);
  }

  .accent-bar {
    position: absolute;
    left: 0; top: 200px;
    width: 12px; height: 116px;
    background: var(--brand-yellow);
  }
  .accent-tab {
    position: absolute;
    right: 0; top: 233px;
    width: 14px; height: 45px;
    background: var(--brand-blue);
  }

  .contact-list {
    position: absolute;
    left: 37px; top: 250px;
    list-style: none;
    font-size: 16px;
    color: var(--ink);
  }
  .contact-list li {
    display: flex;
    align-items: center;
    height: 23px;
  }
  .contact-icon {
    width: 15px; height: 15px;
    margin-right: 10px;
    flex: none;
  }
  .contact-square {
    width: 13px; height: 13px;
    margin: 0 11px 0 1px;
    background: var(--brand-blue);
    flex: none;
  }

  .person {
    position: absolute;
    right: 40px; top: 230px;
    text-align: right;
  }
  .person__name {
    font-size: 23px;
    font-weight: 600;
    color: var(--brand-blue);
    line-height: 28px;
  }
  .person__role {
    font-size: 16px;
    color: var(--brand-yellow);
    line-height: 22px;
  }
</style>
</head>
<body>
  <section class="card card--front">
    <div class="wordmark">Torvane PT</div>
    <div class="accent-bar"></div>
    <ul class="contact-list">
      <li>
        <svg class="contact-icon" viewBox="0 0 24 24" aria-hidden="true">
          <path fill="#0d84c9" d="M6.6 10.8a15.1 15.1 0 0 0 6.6 6.6l2.2-2.2a1 1 0 0 1 1-.25 11.4 11.4 0 0 0 3.6.57 1 1 0 0 1 1 1V20a1 1 0 0 1-1 1A17 17 0 0 1 3 4a1 1 0 0 1 1-1h3.5a1 1 0 0 1 1 1c0 1.25.2 2.45.57 3.57a1 1 0 0 1-.25 1z"/>
        </svg>
        0427309581
      </li>
      <li><span class="contact-square"></span>Torvane PT</li>
    </ul>
    <div class="person">
      <div class="person__name">DAN MERCER</div>
      <div class="person__role">Personal Trainer</div>
    </div>
    <div class="accent-tab"></div>
  </section>

  <section class="card card--back">
    <div class="wordmark">Torvane PT</div>
  </section>
</body>
</html>
```